Steadfast Chiropractic Claims; email ad

Trying to develop an ad that will be placed along other advertisers on an email blast for a chiropractic magazine. See sample of other ads http://www.vertexspinejournal.example/deals_events/

the size is 550 w x 252 H

Font styles to use
Serif

Colors
ec1f27

Requirements
Must have
• Must stand out and make the user want to click on the ad

```html
<!DOCTYPE html>
<html lang="en">
<head>
<meta charset="utf-8">
<title>Steadfast Chiropractic Claims – Email Ad</title>
<link rel="stylesheet" href="https://fonts.googleapis.com/css2?family=Oswald:wght@600&family=Tinos:wght@400;700&family=Saira+Condensed:ital,wght@1,800&display=swap">
<style>
  :root {
    --navy: #0d3a72;
    --blue: #1a5da3;
    --deep-red: #8e1a1f;
    --brand-red: #ec1f27;
    --ink: #111111;
    --white: #ffffff;
    --rule: #c9cbd0;
  }
  html, body { margin: 0; padding: 0; width: 1200px; height: 1200px; overflow: hidden; background: var(--white); }
  .ad {
    position: absolute; left: 75px; top: 317px; width: 1049px; height: 481px;
    overflow: hidden; background: var(--white);
  }
  .ad-bg { position: absolute; inset: 0; }
  .brand {
    position: absolute; left: 32px; top: 70px; width: 170px;
    display: flex; align-items: center; gap: 10px;
    font-family: "Tinos", serif; font-weight: 700; font-size: 30px; color: var(--brand-red);
  }
  .brand-dot { width: 14px; height: 14px; border-radius: 50%; background: var(--brand-red); flex: none; }
  .headline {
    position: absolute; left: 209px; top: 26px; margin: 0;
    font-family: "Oswald", sans-serif; font-weight: 600; color: var(--navy);
    line-height: 1; transform: scaleX(0.8); transform-origin: left top;
    white-space: nowrap;
  }
  .headline span { display: block; }
  .headline .l1 { font-size: 74px; letter-spacing: 1px; height: 80px; }
  .headline .l2 { font-size: 56px; letter-spacing: 2px; }
  .copy {
    position: absolute; left: 14px; top: 0; width: 680px; height: 340px; text-align: center;
    font-family: "Tinos", serif;
  }
  .copy p { position: absolute; left: 0; width: 100%; margin: 0; white-space: nowrap; }
  .tagline { top: 168px; font-size: 24px; line-height: 26px; color: var(--ink); letter-spacing: -0.7px; }
  .claim { top: 199px; font-size: 28px; line-height: 28px; color: var(--deep-red); letter-spacing: -0.2px; }
  .detail { top: 264px; font-size: 20px; line-height: 24px; color: var(--ink); }
  .punch { top: 312px; font-size: 25px; line-height: 28px; font-weight: 700; color: var(--deep-red); }
  .photo {
    position: absolute; left: 721px; top: 19px; width: 296px; height: 424px;
    border-radius: 130px 130px 0 0;
    background: radial-gradient(ellipse at 50% 40%, #c9b19e 0%, #d8d8d8 45%, #f1f1f1 75%, rgba(255,255,255,0) 100%);
  }
  .cta {
    position: absolute; left: 39px; top: 405px; width: 255px; height: 54px;
    box-sizing: border-box; border: 3px solid var(--white); border-radius: 27px;
    background: linear-gradient(#c22a2e, var(--deep-red));
    box-shadow: 0 3px 6px rgba(0,0,0,0.35);
    display: flex; align-items: center; justify-content: center; gap: 8px;
    font-family: "Saira Condensed", sans-serif; font-style: italic; font-weight: 800;
    font-size: 32px; color: var(--white);
  }
  .phone {
    position: absolute; left: 365px; top: 402px;
    font-family: "Saira Condensed", sans-serif; font-style: italic; font-weight: 800;
    font-size: 54px; color: var(--white); letter-spacing: 1px;
    text-shadow: 0 2px 4px rgba(0,0,0,0.4);
  }
  .web {
    position: absolute; left: 825px; top: 446px;
    font-family: "Saira Condensed", sans-serif; font-style: italic; font-weight: 800;
    font-size: 19px; color: var(--white);
  }
</style>
</head>
<body>
<div class="ad">
  <svg class="ad-bg" width="1049" height="481" viewBox="0 0 1049 481" aria-hidden="true">
    <defs>
      <radialGradient id="mist" cx="0.85" cy="0.1" r="0.6">
        <stop offset="0" stop-color="#dcdde0"/>
        <stop offset="1" stop-color="#ffffff"/>
      </radialGradient>
    </defs>
    <rect width="1049" height="481" fill="url(#mist)"/>
    <path d="M0 322 C 150 360, 350 395, 520 398 C 700 400, 900 352, 1049 318 L1049 481 L0 481 Z" fill="var(--blue)"/>
    <path d="M0 316 C 150 352, 350 386, 520 390" stroke="var(--rule)" stroke-width="3" fill="none"/>
    <path d="M0 308 C 150 344, 350 378, 520 382" stroke="var(--rule)" stroke-width="2" fill="none" opacity="0.7"/>
    <path d="M220 372 C 420 356, 620 300, 1049 180 L1049 262 C 760 318, 480 378, 220 374 Z" fill="var(--deep-red)"/>
    <path d="M685 481 C 800 458, 930 438, 1049 427 L1049 481 Z" fill="var(--deep-red)"/>
  </svg>

  <div class="photo" role="img" aria-label="Photo of a chiropractor adjusting a smiling patient's neck"></div>

  <div class="brand"><span class="brand-dot"></span>Steadfast</div>

  <h1 class="headline"><span class="l1">TIRED OF FIGHTING</span><span class="l2">INSURANCE COMPANY?</span></h1>

  <div class="copy">
    <p class="tagline">Let us help keep your business as healthy as you keep your patients</p>
    <p class="claim">Steadfast employs past insurance claim examiners,<br>we have the "inside" information.</p>
    <p class="detail">We know the laws and the resgulations to make the insurance<br>companies do what thet are supposed to do,</p>
    <p class="punch">PAY THE CLAIM!</p>
  </div>

  <div class="cta">
    <svg width="22" height="24" viewBox="0 0 22 24" aria-hidden="true"><path d="M3 2 L17 12 L3 22 L8 12 Z" fill="#fff"/></svg>
    GET MORE INFO
  </div>
  <div class="phone">844-555-0173</div>
  <div class="web">STEADFASTCHIROCLAIMS.COM</div>
</div>
</body>
</html>
```